Website for UK Fintech Company specialising in Auto-Finance asset management

We need a website for a FINTECH business called KELP Asset Management. We have developed and licenced an innovative platform to provide financial institutions whom provide secured Asset finance loans to consumer and commercial clients, allowing for real time tracking and management of defaulted accounts pending repossession. The kelp asset management platform is a total recoveries solution through the cycle, from the moment the lender has to recover the vehicle (due to default/non-payment) to the disposal of the vehicle (via sale at Motor Auctions or by selling to a Car dealership network). The data provided from external services allows the Financier to make informed decisions, such as whether it is economical to continue the recovery and decide which sales channel is better suited for their assets to maximise residual values and minimise financial losses. The KELP platform provides an array of MI reporting and uses a systematic approach utilising exception reporting to identify key areas of non-performance to enable focus where needed. KELP also provides a leading Debt collection service recovering end-of-cycle losses such as Financial Shortfall and losses in vehicle values due to conditions and excessive damage.

We also require a new logo for out new product called MB-Prismo

Target Market(s)

Financial institutions whom provide secured Asset finance loans to consumer and commercial clients

Industry/Entity Type

Financial Service

Logo Text

MB- Prismo (this is for a new product which forms part of the KELP Asset Mangement Platform

Number of Pages Required

4 page

Font styles to use
Serif
Sans Serif

Colors

Designer to choose colors to be used in the design.

Requirements
Must have
• We need a simple website with a broken down as follows;
• • Landing page
• • Services page
• • About us page
• • kelp asset management platform login page (client facing)
Nice to have
• Our slogan is 'Auto-Finance Expertise'
• We are very much open to suggestions as long as we can create a professional/ corporate / modern feel to the website. We are a FINTECH company, and that needs to come across
Should not have
• Whilst we are an asset management company primarily managing vehicles through our platform, we don't want it to look like a car dealership website!:)

```html
<!DOCTYPE html>
<html lang="en">
<head>
<meta charset="utf-8">
<title>KELP Asset Management</title>
<link rel="stylesheet" href="https://fonts.googleapis.com/css2?family=Oswald:wght@400;500;600&family=PT+Sans:wght@400;700&display=swap">
<style>
:root{
  --orange:#f07c00;
  --orange-dark:#d96f00;
  --ink:#222;
  --text:#777;
  --light:#f6f6f6;
  --ghost:#ebebeb;
  --white:#fff;
  --footer:#2a2a2a;
  --footer-bottom:#1c1c1c;
  --photo-dark:#5a5350;
  --photo-mid:#a9a5a2;
}
*{box-sizing:border-box;margin:0;padding:0}
html,body{width:1200px;height:3509px;overflow:hidden}
body{position:relative;background:var(--white);font-family:"PT Sans",Arial,sans-serif;color:var(--text)}
.abs{position:absolute}

/* hero */
.hero{left:0;top:0;width:1200px;height:617px;background:var(--white);overflow:hidden}
.hero-photo{left:0;top:0;width:1200px;height:617px;background:linear-gradient(100deg,var(--photo-dark) 0%,#8a8480 35%,var(--photo-mid) 60%,#d9d7d5 85%,#bbb 100%);clip-path:polygon(440px 0,1200px 0,1200px 617px,40px 617px,0 580px,0 0)}
.hero-shade{left:0;top:0;width:1200px;height:617px;background:linear-gradient(180deg,rgba(0,0,0,.35),rgba(0,0,0,0) 30%,rgba(0,0,0,.15));pointer-events:none}
.hero-corner{left:0;top:0;width:460px;height:617px;background:var(--white);clip-path:polygon(0 0,440px 0,0 460px)}
.brand{left:199px;top:28px;font-family:"PT Sans",sans-serif;font-weight:700;font-size:46px;color:var(--ink);line-height:1}
.brand-tag{left:199px;top:80px;font-size:9px;letter-spacing:.3px;color:var(--orange);text-transform:uppercase;white-space:nowrap}
.topbar{left:618px;top:32px;display:flex;gap:30px;font-size:13px;color:var(--white)}
.topbar span{display:flex;align-items:center;gap:8px}
.nav{left:548px;top:68px;display:flex;gap:38px;font-size:13px;font-weight:700;color:var(--white)}
.nav .active{color:var(--orange)}
.hero-title{left:500px;top:255px;width:501px;text-align:right;font-family:"Oswald",sans-serif;font-weight:500;font-size:46px;color:var(--white);letter-spacing:.5px}
.hero-sub{left:500px;top:322px;width:501px;text-align:right;font-size:16px;font-weight:700;color:var(--white)}
.btn{display:flex;align-items:center;justify-content:center;background:var(--orange);color:var(--white);font-size:13px;font-weight:700;text-transform:uppercase}
.hero-btn{left:870px;top:374px;width:131px;height:52px;font-size:15px}
.dots{left:962px;top:470px;display:flex;gap:5px}
.dots i{width:10px;height:10px;border-radius:50%;background:var(--white);display:block}
.dots i.on{background:var(--orange)}

/* sections */
.services{left:0;top:617px;width:1200px;height:735px;background:var(--light)}
.ghost{width:1200px;text-align:center;font-family:"Oswald",sans-serif;font-weight:600;color:var(--ghost);line-height:1;letter-spacing:4px}
.section-title{width:1200px;text-align:center;font-family:"Oswald",sans-serif;font-weight:500;font-size:40px;color:var(--orange)}
.card{background:var(--white);width:246px;height:238px;overflow:hidden;text-align:center}
.card::after{content:"";position:absolute;right:0;bottom:0;width:26px;height:26px;background:var(--orange);clip-path:polygon(100% 0,100% 100%,0 100%)}
.card svg{margin-top:38px}
.card h3{font-family:"Oswald",sans-serif;font-weight:500;font-size:16px;color:var(--orange);margin-top:10px}
.card p{font-size:12px;line-height:19px;margin:8px 26px 0}
.more-btn{left:517px;width:166px;height:49px;font-size:12px}

.platform{left:0;top:1352px;width:1200px;height:468px}
.platform-orange{left:0;top:0;width:643px;height:468px;background:linear-gradient(90deg,#e98a2a,var(--orange) 60%)}
.platform-photo{left:643px;top:0;width:557px;height:468px;background:linear-gradient(120deg,#d7cfc9,#efe9e4 40%,#c5c9d2 75%,#e9e6e2)}
.platform h2{left:199px;top:72px;font-family:"Oswald",sans-serif;font-weight:500;font-size:38px;color:var(--white)}
.platform h4{left:199px;top:134px;width:400px;font-size:15px;line-height:23px;font-weight:700;color:var(--white)}
.platform p{left:199px;top:198px;width:420px;font-size:12.5px;line-height:23px;color:var(--white)}
.learn-btn{left:199px;top:353px;width:117px;height:49px;background:var(--white);color:var(--orange-dark);font-size:12px}

.about{left:0;top:1820px;width:1200px;height:381px;background:var(--white);border-bottom:1px solid #e6e6e6}
.about p{left:200px;top:278px;width:800px;text-align:center;font-size:12.5px;line-height:23px}

.product{left:0;top:2201px;width:1200px;height:306px;background:var(--white)}
.product h3{width:1200px;top:32px;text-align:center;font-family:"Oswald",sans-serif;font-weight:500;font-size:25px;color:var(--orange)}
.product-name{left:0;top:112px;width:1200px;text-align:center;font-family:"PT Sans",sans-serif;font-weight:700;font-size:34px;color:var(--ink);letter-spacing:2px}
.product p{left:250px;top:222px;width:700px;text-align:center;font-size:12.5px;line-height:22px}

.news{left:0;top:2507px;width:1200px;height:761px;background:var(--light)}
.news-card{width:257px;height:400px;background:var(--white);box-shadow:0 2px 6px rgba(0,0,0,.12)}
.news-img{width:257px;height:169px}
.news-date{left:18px;top:196px;font-size:11px;font-weight:700;color:var(--ink)}
.news-title{left:18px;top:222px;width:222px;font-size:14px;line-height:20px;color:var(--orange)}
.news-text{left:18px;top:276px;width:222px;font-size:12px;line-height:19px}
.news-rule{left:18px;top:340px;width:222px;height:1px;background:#e3e3e3}
.news-meta{left:18px;top:357px;display:flex;gap:22px;font-size:11px}
.news-meta span{display:flex;align-items:center;gap:6px}
.arrow{width:34px;height:34px;border-radius:50%;background:var(--ink);display:flex;align-items:center;justify-content:center}

.footer{left:0;top:3268px;width:1200px;height:198px;background:var(--footer);color:#bbb}
.footer h5{font-family:"Oswald",sans-serif;font-weight:400;font-size:17px;color:var(--white)}
.footer .small{font-size:11px;color:var(--orange);letter-spacing:.5px}
.footer .line{display:flex;align-items:center;gap:12px;font-size:13px;color:var(--orange)}
.social{display:flex;gap:22px}
.social i{width:14px;height:14px;border-radius:50%;background:var(--white);display:block}
.email-field{left:690px;top:109px;width:199px;height:36px;background:#1e1e1e;color:#999;font-size:11px;padding:11px 14px;letter-spacing:1px}
.sub-btn{left:893px;top:109px;width:108px;height:36px;font-size:11px}
.footer-bottom{left:0;top:3466px;width:1200px;height:43px;background:var(--footer-bottom);font-size:11px;color:#aaa}
.footer-links{left:199px;top:14px;display:flex;gap:14px}
.footer-links b{font-weight:400;color:#666}
.copyright{right:199px;top:14px}
.copyright em{font-style:normal;color:var(--orange)}
</style>
</head>
<body>

<header class="abs hero">
  <div class="abs hero-photo" role="img" aria-label="Photo of a businesswoman holding a folder in a car showroom"></div>
  <div class="abs hero-shade"></div>
  <div class="abs hero-corner"></div>
  <div class="abs brand">KELP</div>
  <div class="abs brand-tag">Asset management platform</div>
  <div class="abs topbar">
    <span><svg width="13" height="13" viewBox="0 0 24 24"><path fill="#fff" d="M6.6 10.8a15.1 15.1 0 0 0 6.6 6.6l2.2-2.2a1 1 0 0 1 1-.25 11.4 11.4 0 0 0 3.6.57 1 1 0 0 1 1 1V20a1 1 0 0 1-1 1A17 17 0 0 1 3 4a1 1 0 0 1 1-1h3.5a1 1 0 0 1 1 1c0 1.25.2 2.45.57 3.57a1 1 0 0 1-.25 1z"/></svg>+1555012347</span>
    <span><svg width="15" height="11" viewBox="0 0 24 18"><rect width="24" height="18" fill="#fff"/><path d="M0 0l12 9 12-9" fill="none" stroke="#777" stroke-width="2"/></svg>info@kelpassetplatform.com</span>
  </div>
  <nav class="abs nav"><span class="active">Home</span><span>Services</span><span>About Us</span><span>KELP Asset Management</span><span>Login</span></nav>
  <h1 class="abs hero-title">AUTO-FINANCE EXPERTISE</h1>
  <p class="abs hero-sub">Fintech Company specializing in Auto-Finance asset management</p>
  <a class="abs btn hero-btn">Contact us</a>
  <div class="abs dots"><i></i><i class="on"></i></div>
</header>

<section class="abs services">
  <div class="abs ghost" style="top:62px;font-size:230px">SERVICES</div>
  <h2 class="abs section-title" style="top:150px">Services We Provided</h2>
  <article class="abs card" style="left:201px;top:333px">
    <svg width="80" height="52" viewBox="0 0 80 52" fill="none" stroke="#222" stroke-width="3"><circle cx="16" cy="14" r="11"/><path d="M16 8v12M13 11h5M13 17h5"/><path d="M22 36l6-12h28l8 12h8v10H14V36z"/><circle cx="28" cy="46" r="5" fill="#fff"/><circle cx="58" cy="46" r="5" fill="#fff"/></svg>
    <h3>Auto Finance</h3>
    <p>Lorem Ipsum is simply dummy text of the printing and typesetting industry. Lorem Ipsum has been the industry's</p>
  </article>
  <article class="abs card" style="left:477px;top:333px">
    <svg width="60" height="52" viewBox="0 0 60 52" fill="none" stroke="#222" stroke-width="3"><path d="M6 16L30 4l24 12z"/><path d="M12 20v20M24 20v20M36 20v20M48 20v20"/><path d="M4 44h52M2 50h56"/></svg>
    <h3>Asset finance</h3>
    <p>Lorem Ipsum is simply dummy text of the printing and typesetting industry. Lorem Ipsum has been the industry's</p>
  </article>
  <article class="abs card" style="left:751px;top:333px">
    <svg width="64" height="52" viewBox="0 0 64 52" fill="none" stroke="#222" stroke-width="3"><path d="M6 24L28 4l22 20"/><path d="M12 20v28h18"/><path d="M22 48V32h10"/><ellipse cx="46" cy="32" rx="12" ry="4"/><path d="M34 32v12c0 2 5 4 12 4s12-2 12-4V32M34 38c0 2 5 4 12 4s12-2 12-4"/></svg>
    <h3>Asset Management</h3>
    <p>Lorem Ipsum is simply dummy text of the printing and typesetting industry. Lorem Ipsum has been the industry's</p>
  </article>
  <a class="abs btn more-btn" style="top:625px">View more services</a>
</section>

<section class="abs platform">
  <div class="abs platform-orange"></div>
  <div class="abs platform-photo" role="img" aria-label="Photo of a couple reviewing finance paperwork together"></div>
  <h2 class="abs">KELP Asset Management</h2>
  <h4 class="abs">We have developed and licensed an innovative platform to provide financial institutions</h4>
  <p class="abs">Lorem Ipsum is simply dummy text of the printing and typesetting industry. Lorem Ipsum has been the industry's standard dummy text ever since the 1500s, when an unknown printer took a galley of type and scrambled it to make a type specimen book. It has survived not only five centuries, but also the leap into electronic typesetting.</p>
  <a class="abs btn learn-btn">Learn more</a>
</section>

<section class="abs about">
  <div class="abs ghost" style="top:48px;font-size:200px">ABOUT US</div>
  <h2 class="abs section-title" style="top:112px">About Us</h2>
  <p class="abs">Lorem Ipsum is simply dummy text of the printing and typesetting industry. Lorem Ipsum has been the industry's standard dummy text ever since the 1500s, when an unknown printer took a galley of type and scrambled it to make a type specimen book. It has survived not only five centuries, but also the leap into electronic typesetting, remaining essentially unchanged. It was popularised software like Aldus...</p>
</section>

<section class="abs product">
  <h3 class="abs">Our New Product</h3>
  <div class="abs product-name">MB-Prismo</div>
  <p class="abs">Lorem Ipsum is simply dummy text of the printing and typesetting industry. Lorem Ipsum has been the industry's standard dummy text ever since the 1500s, when an unknown printer took a galley of type and scrambled</p>
</section>

<section class="abs news">
  <div class="abs ghost" style="top:42px;font-size:190px">NEWS</div>
  <h2 class="abs section-title" style="top:130px">Latest News</h2>

  <article class="abs news-card" style="left:201px;top:302px">
    <div class="abs news-img" style="background:linear-gradient(120deg,#d9d3cf,#b9b2ae 50%,#e6e3e0)" role="img" aria-label="Photo of a businesswoman in a car showroom"></div>
    <div class="abs news-date">FEB 28-2018</div>
    <div class="abs news-title">Lorem Ipsum is simply dummy text of the printing and text.</div>
    <div class="abs news-text">Lorem Ipsum is simply dummy text of the printing and typesetting industry. Lorem Ipsum has been type...</div>
    <div class="abs news-rule"></div>
    <div class="abs news-meta"><span><svg width="13" height="11" viewBox="0 0 13 11"><rect x=".5" y=".5" width="12" height="8" fill="none" stroke="#888"/><path d="M3 8.5v2l3-2" fill="none" stroke="#888"/></svg>Comment</span><span><svg width="11" height="11" viewBox="0 0 11 11"><rect x=".5" y=".5" width="10" height="10" fill="none" stroke="#888"/><circle cx="5.5" cy="4.5" r="2" fill="#888"/></svg>Tom Archer</span></div>
  </article>

  <article class="abs news-card" style="left:472px;top:302px">
    <div class="abs news-img" style="background:linear-gradient(120deg,#cfc9c4,#9a948f 50%,#ddd8d2)" role="img" aria-label="Photo of a business team meeting at a table"></div>
    <div class="abs news-date">FEB 28-2018</div>
    <div class="abs news-title">Lorem Ipsum is simply dummy text of the printing and text.</div>
    <div class="abs news-text">Lorem Ipsum is simply dummy text of the printing and typesetting industry. Lorem Ipsum has been type...</div>
    <div class="abs news-rule"></div>
    <div class="abs news-meta"><span><svg width="13" height="11" viewBox="0 0 13 11"><rect x=".5" y=".5" width="12" height="8" fill="none" stroke="#888"/><path d="M3 8.5v2l3-2" fill="none" stroke="#888"/></svg>Comment</span><span><svg width="11" height="11" viewBox="0 0 11 11"><rect x=".5" y=".5" width="10" height="10" fill="none" stroke="#888"/><circle cx="5.5" cy="4.5" r="2" fill="#888"/></svg>Tom Archer</span></div>
  </article>

  <article class="abs news-card" style="left:746px;top:302px">
    <div class="abs news-img" style="background:linear-gradient(120deg,#e4e6ea,#b8bcc4 50%,#eceef0)" role="img" aria-label="Photo of hands working with a calculator and documents"></div>
    <div class="abs news-date">FEB 28-2018</div>
    <div class="abs news-title">Lorem Ipsum is simply dummy text of the printing and text.</div>
    <div class="abs news-text">Lorem Ipsum is simply dummy text of the printing and typesetting industry. Lorem Ipsum has been type...</div>
    <div class="abs news-rule"></div>
    <div class="abs news-meta"><span><svg width="13" height="11" viewBox="0 0 13 11"><rect x=".5" y=".5" width="12" height="8" fill="none" stroke="#888"/><path d="M3 8.5v2l3-2" fill="none" stroke="#888"/></svg>Comment</span><span><svg width="11" height="11" viewBox="0 0 11 11"><rect x=".5" y=".5" width="10" height="10" fill="none" stroke="#888"/><circle cx="5.5" cy="4.5" r="2" fill="#888"/></svg>Tom Archer</span></div>
  </article>

  <div class="abs arrow" style="left:175px;top:519px"><svg width="10" height="14" viewBox="0 0 10 14"><path d="M8 1L2 7l6 6" fill="none" stroke="#fff" stroke-width="2.5"/></svg></div>
  <div class="abs arrow" style="left:991px;top:519px"><svg width="10" height="14" viewBox="0 0 10 14"><path d="M2 1l6 6-6 6" fill="none" stroke="#fff" stroke-width="2.5"/></svg></div>
</section>

<footer class="abs footer">
  <h5 class="abs" style="left:199px;top:44px">Contact Us</h5>
  <div class="abs line" style="left:199px;top:92px"><svg width="14" height="14" viewBox="0 0 24 24"><path fill="#f07c00" d="M6.6 10.8a15.1 15.1 0 0 0 6.6 6.6l2.2-2.2a1 1 0 0 1 1-.25 11.4 11.4 0 0 0 3.6.57 1 1 0 0 1 1 1V20a1 1 0 0 1-1 1A17 17 0 0 1 3 4a1 1 0 0 1 1-1h3.5a1 1 0 0 1 1 1c0 1.25.2 2.45.57 3.57a1 1 0 0 1-.25 1z"/></svg>+1555012347</div>
  <div class="abs line" style="left:199px;top:126px;font-size:11px"><svg width="14" height="10" viewBox="0 0 24 18"><rect width="24" height="18" fill="#f07c00"/><path d="M0 0l12 9 12-9" fill="none" stroke="#2a2a2a" stroke-width="2"/></svg>info@kelpassetplatform.com</div>

  <h5 class="abs" style="left:510px;top:44px">Connect With Us</h5>
  <div class="abs small" style="left:490px;top:74px;text-transform:uppercase">Social media channels</div>
  <div class="abs social" style="left:510px;top:108px"><i></i><i></i><i></i><i></i></div>

  <h5 class="abs" style="left:690px;top:44px">Newsletter</h5>
  <div class="abs small" style="left:690px;top:74px;text-transform:uppercase">Sign up for special offers</div>
  <div class="abs email-field">EMAIL</div>
  <a class="abs btn sub-btn">Subscribe</a>
</footer>

<div class="abs footer-bottom">
  <div class="abs footer-links"><span>Home</span><b>/</b><span>About Us</span><b>/</b><span>Services</span><b>/</b><span>KELP Asset Management</span><b>/</b><span>Login</span></div>
  <div class="abs copyright">© Copyright 2018 <em>kelp asset management platform</em></div>
</div>

</body>
</html>
```